Real Estate Entrepreneur needs a business card

I am a real estate entrepreneur, I buy houses for investment purposes, I act as a real estate agent representing buyers and sellers in residential home transactions, I am a contractor that does a wide range of home repairs and construction. I'd like a design that can stick with me through the years as my business grows and morphs to fit any niche I decide to pursue as markets change.

Target Market(s)

Anyone with interest that may be related to real estate.

Industry/Entity Type

Real Estate

Contact Information for Business Card

A card that stands out and doesn't put me in any one box. My business will evolve over time and I need a card that can stay relevant.

Colors

Designer to choose colors to be used in the design.

Requirements
Must have
• Character
Nice to have
• I'm open
Should not have
• Cliche houses and hammers

```html
<!DOCTYPE html>
<html lang="en">
<head>
<meta charset="utf-8">
<title>Reid Calder – Business Card</title>
<link href="https://fonts.googleapis.com/css2?family=Oswald:wght@500&family=Roboto:wght@400&display=swap" rel="stylesheet">
<style>
  :root {
    --brand-blue: #234a8f;
    --ink: #111111;
    --paper: #ffffff;
  }
  html, body {
    margin: 0;
    padding: 0;
    width: 1200px;
    height: 720px;
    overflow: hidden;
    background: var(--paper);
  }
  .card {
    position: relative;
    width: 1200px;
    height: 720px;
    background: var(--paper);
    overflow: hidden;
  }
  .name-frame,
  .contact-icons {
    position: absolute;
    left: 0;
    top: 0;
  }
  .name {
    position: absolute;
    left: 0;
    width: 1200px;
    top: 212px;
    margin: 0;
    text-align: center;
    font-family: "Oswald", "Arial Narrow", sans-serif;
    font-weight: 500;
    font-size: 68px;
    line-height: 1;
    letter-spacing: 1px;
    color: var(--brand-blue);
    text-transform: uppercase;
    white-space: nowrap;
  }
  .role {
    position: absolute;
    left: 0;
    width: 1200px;
    top: 297px;
    margin: 0;
    text-align: center;
    font-family: "Roboto", Arial, sans-serif;
    font-size: 27px;
    line-height: 32px;
    color: var(--ink);
    white-space: nowrap;
  }
  .contact-list {
    position: absolute;
    left: 0;
    width: 1200px;
    top: 467px;
    margin: 0;
    padding: 0;
    list-style: none;
    text-align: center;
    font-family: "Roboto", Arial, sans-serif;
    font-size: 27px;
    line-height: 39px;
    color: var(--ink);
    letter-spacing: 0.5px;
  }
  .footer-band {
    position: absolute;
    left: 0;
    bottom: 0;
    width: 1200px;
    height: 80px;
    background: var(--brand-blue);
  }
</style>
</head>
<body>
<main class="card">
  <svg class="name-frame" width="1200" height="720" viewBox="0 0 1200 720" aria-hidden="true">
    <path d="M430 314 H388 V197 H812 V314 H766" fill="none" stroke="var(--ink)" stroke-width="4.5"/>
  </svg>

  <h1 class="name">Reid Calder</h1>
  <p class="role">Real Estate Entrepreneur</p>

  <svg class="contact-icons" width="1200" height="720" viewBox="0 0 1200 720" aria-hidden="true">
    <g class="icon-phone" fill="var(--brand-blue)">
      <path d="M571 412 c-2 0 -4 2 -3 5 c2 7 8 13 15 15 c3 1 5 -1 5 -3 l0 -3 c0 -1 -1 -2 -2 -2 l-4 -1 c-1 0 -2 0 -2 1 l-1 2 c-3 -1 -6 -4 -7 -7 l2 -1 c1 0 1 -1 1 -2 l-1 -4 c0 -1 -1 -2 -2 -2 z"/>
      <path d="M580 412 a8 8 0 0 1 8 8" fill="none" stroke="var(--brand-blue)" stroke-width="2"/>
      <path d="M580 416 a4 4 0 0 1 4 4" fill="none" stroke="var(--brand-blue)" stroke-width="2"/>
    </g>
    <g class="icon-mail" fill="var(--brand-blue)">
      <rect x="606" y="412" width="24" height="18" rx="2"/>
      <path d="M607 414 L618 423 L629 414" fill="none" stroke="var(--paper)" stroke-width="1.8"/>
    </g>
    <path class="divider" d="M540 445 Q600 442 660 445 Q600 448 540 445 Z" fill="var(--ink)" stroke="var(--ink)" stroke-width="1"/>
  </svg>

  <ul class="contact-list">
    <li class="phone">123 456 7890</li>
    <li class="email">info@example.com</li>
  </ul>

  <div class="footer-band"></div>
</main>
</body>
</html>
```